Bag Design For Frozen Prawns

Basically we need a design for a plastic bag that we have packed in Vietnam. I have attached a copy of our logo a picture of a bag I like.
As you can see it is simple clean and fresh.

Target Market(s)

Chefs

Industry/Entity Type

Plastic

```html
<!DOCTYPE html>
<html lang="en">
<head>
<meta charset="utf-8">
<title>Tidehouse – Uncooked Shrimp Bag</title>
<link rel="stylesheet" href="https://fonts.googleapis.com/css2?family=Montserrat:wght@500;700&display=swap">
<style>
  :root {
    --page: #ffffff;
    --seal: #e4e4e4;
    --seal-line: #c9c9c9;
    --foil-light: #f4f4f4;
    --foil-mid: #d8d8d8;
    --foil-dark: #a9a9a9;
    --ink: #141414;
    --art-light: #e6e6e6;
    --art-dark: #9a9a9a;
  }
  * { margin: 0; padding: 0; box-sizing: border-box; }
  html, body { width: 1200px; height: 1200px; overflow: hidden; background: var(--page); }
  .canvas { position: relative; width: 1200px; height: 1200px; }
  .bag { position: absolute; left: 316px; top: 12px; width: 568px; height: 1170px; }
  .bag-shape { position: absolute; inset: 0; width: 100%; height: 100%; }
  .brand {
    position: absolute; left: 0; right: 0; top: 386px;
    display: flex; align-items: center; justify-content: center; gap: 12px;
    font-family: "Montserrat", sans-serif; font-weight: 700; font-size: 27px;
    color: var(--ink); letter-spacing: 0.5px;
  }
  .brand-dot { width: 30px; height: 30px; border-radius: 50%; background: var(--ink); }
  .product-art {
    position: absolute; left: 32px; top: 540px; width: 504px; height: 246px;
    background: radial-gradient(ellipse at 50% 50%, var(--art-light) 0%, var(--art-dark) 100%);
    border-radius: 6px;
  }
  .product-name {
    position: absolute; left: 0; right: 0; top: 846px; text-align: center;
    font-family: "Montserrat", sans-serif; font-weight: 500; color: var(--ink);
    line-height: 1.05;
  }
  .product-name .state { display: block; font-size: 38px; }
  .product-name .kind { display: block; font-size: 30px; letter-spacing: 1px; }
</style>
</head>
<body>
<div class="canvas">
  <div class="bag">
    <svg class="bag-shape" viewBox="0 0 568 1170" aria-hidden="true">
      <defs>
        <linearGradient id="foil" x1="0" x2="1" y1="0" y2="0">
          <stop offset="0" stop-color="var(--foil-dark)"/>
          <stop offset="0.25" stop-color="var(--foil-mid)"/>
          <stop offset="0.5" stop-color="var(--foil-light)"/>
          <stop offset="0.75" stop-color="var(--foil-mid)"/>
          <stop offset="1" stop-color="var(--foil-dark)"/>
        </linearGradient>
        <pattern id="teeth-top" width="16" height="8" patternUnits="userSpaceOnUse">
          <polygon points="0,0 16,0 8,8" fill="var(--page)"/>
        </pattern>
        <pattern id="teeth-bottom" width="16" height="8" patternUnits="userSpaceOnUse">
          <polygon points="0,8 16,8 8,0" fill="var(--page)"/>
        </pattern>
      </defs>
      <!-- top seal -->
      <rect class="seal-top" x="0" y="0" width="568" height="156" fill="var(--seal)"/>
      <rect x="0" y="0" width="568" height="8" fill="url(#teeth-top)"/>
      <g stroke="var(--seal-line)" stroke-width="1.5">
        <line x1="0" y1="30" x2="568" y2="30"/>
        <line x1="0" y1="44" x2="568" y2="44"/>
        <line x1="0" y1="120" x2="568" y2="120"/>
        <line x1="0" y1="134" x2="568" y2="134"/>
      </g>
      <circle class="hang-hole" cx="284" cy="70" r="7" fill="var(--page)" stroke="var(--seal-line)"/>
      <!-- foil body -->
      <rect class="body" x="0" y="156" width="568" height="810" fill="url(#foil)"/>
      <!-- dark base band -->
      <path class="base-band" d="M0,816 Q284,1056 568,816 L568,966 L0,966 Z" fill="var(--ink)"/>
      <!-- bottom seal -->
      <rect class="seal-bottom" x="0" y="966" width="568" height="204" fill="var(--seal)"/>
      <rect x="0" y="1162" width="568" height="8" fill="url(#teeth-bottom)"/>
      <g stroke="var(--seal-line)" stroke-width="1.5">
        <line x1="0" y1="994" x2="568" y2="994"/>
        <line x1="0" y1="1008" x2="568" y2="1008"/>
        <line x1="0" y1="1128" x2="568" y2="1128"/>
        <line x1="0" y1="1142" x2="568" y2="1142"/>
      </g>
    </svg>

    <div class="brand">
      <span class="brand-dot"></span>
      <span class="brand-name">TIDEHOUSE</span>
    </div>

    <div class="product-art" role="img" aria-label="Black line illustration of a shrimp curled over a flowing wave line"></div>

    <p class="product-name">
      <span class="state">uncooked</span>
      <span class="kind">shrimp</span>
    </p>
  </div>
</div>
</body>
</html>
```